nutrition ebook cover

i need a cover for a ebook designed, the book is called velvet ridge so i would like that somewhere on the cover. i would also like the word nutrition followed by my company logo that i have attached below somewhere on the cover( i have attached two logos and would like to see with both separatley), i would like this to be faded into the background if possible, perhaps in a upper or lower corner. i would also like to see options with and without the picture i have attached below. the look I'm going for is professional and clean. this is a fat loss, healthy eating booklet. the winning designer i would like to design the following pages within the book aswell no more than 10 pages, that i will provide all content for, i just need help with putting what i have on pdf in a way that looks professional and cool. this would ideally covered in the rate that is paid for the cover. i also have other booklets i need made so the winning designer will most likely get that work too at a later date for an additional fee of course.

Industry/Entity Type

Nutrition

Requirements
Nice to have
• Outside images are welcomed, happy to purchase any stock images used from a outside source

```html
<!DOCTYPE html>
<html lang="en">
<head>
<meta charset="utf-8">
<title>Velvet Ridge – Nutrition Ebook Cover</title>
<link rel="stylesheet" href="https://fonts.googleapis.com/css2?family=Poppins:wght@600&display=swap">
<style>
  :root {
    --page-bg: #ffffff;
    --ink: #0c1a10;
    --greens-dark: #1f3a1c;
    --greens-mid: #4f8a2e;
    --greens-light: #9cc25a;
    --mist: #ecefec;
    --slate: #3a4a48;
    --board: #8a5a36;
    --badge: #ffffff;
    --label: rgba(255, 255, 255, 0.82);
  }
  * { margin: 0; padding: 0; box-sizing: border-box; }
  html, body {
    width: 1200px;
    height: 1200px;
    overflow: hidden;
    background: var(--page-bg);
  }
  .canvas {
    position: relative;
    width: 1200px;
    height: 1200px;
  }
  .cover {
    position: absolute;
    left: 279px;
    top: 126px;
    width: 642px;
    height: 949px;
    overflow: hidden;
  }
  .cover-photo {
    position: absolute;
    inset: 0;
    background:
      radial-gradient(ellipse 45% 30% at 28% 22%, #2f6a1e 0%, rgba(47,106,30,0) 100%),
      radial-gradient(ellipse 45% 40% at 78% 28%, #1b2c1c 0%, rgba(27,44,28,0) 100%),
      radial-gradient(ellipse 40% 22% at 50% 88%, var(--board) 0%, rgba(138,90,54,0) 100%),
      linear-gradient(180deg,
        var(--greens-light) 0%,
        var(--greens-mid) 15%,
        var(--greens-dark) 34%,
        #6a7f64 42%,
        var(--mist) 48%,
        var(--mist) 58%,
        #b9c0ba 66%,
        var(--slate) 80%,
        #2d3937 100%);
  }
  .brand-lockup {
    position: absolute;
    top: 42px;
    left: 0;
    right: 0;
    height: 128px;
  }
  .brand-label {
    position: absolute;
    right: 397px;
    top: 46px;
    font-family: "Poppins", sans-serif;
    font-weight: 600;
    font-size: 28px;
    line-height: 36px;
    color: var(--label);
    letter-spacing: 1px;
  }
  .brand-mark {
    position: absolute;
    left: 257px;
    top: 0;
    width: 128px;
    height: 128px;
    border-radius: 50%;
    background: var(--badge);
    display: flex;
    align-items: center;
    justify-content: center;
  }
  .brand-name {
    font-family: "Poppins", sans-serif;
    font-weight: 600;
    font-size: 22px;
    color: var(--ink);
    letter-spacing: 0.5px;
  }
  .title {
    font-family: "Poppins", sans-serif;
    font-weight: 600;
    color: var(--ink);
  }
  .title-line {
    position: absolute;
    left: 0;
    right: 0;
    display: block;
    text-align: center;
    line-height: 1;
    letter-spacing: -3px;
  }
  .title-line--top {
    top: 455px;
    font-size: 150px;
  }
  .title-line--bottom {
    top: 580px;
    font-size: 130px;
  }
</style>
</head>
<body>
  <main class="canvas">
    <section class="cover">
      <div class="cover-photo" role="img" aria-label="Green smoothie glass beside kale, celery and limes above; wooden chopping board surrounded by broccoli, mushrooms, potatoes, tomatoes and herbs below, fading into a light band in the middle"></div>
      <div class="brand-lockup">
        <span class="brand-label">nutrition</span>
        <div class="brand-mark">
          <span class="brand-name">Fernhold</span>
        </div>
      </div>
      <h1 class="title">
        <span class="title-line title-line--top">velvet</span>
        <span class="title-line title-line--bottom">ridge</span>
      </h1>
    </section>
  </main>
</body>
</html>
```